14 years in business and its time for a new look and feel brochure and business cards!

We are looking to create a brochure that is professional and eye catching to bring in new commercial business. After14 years in business we have finally redone our logo and it is time to get a brochure completed as well. The logo that should be used is the one that says Inc. We want this new brochure to appeal to corporate property management companies and smaller apartment complexes. We want it to look rich and have the same high quality our work has.

Target Market(s)

property management companies and apartment complexes in the DMV.

Industry/Entity Type

Construction Company

Contact Information for Business Card

Logo
Dovid Rennick
CEO
Mobile 410-555-0137
Office 410-555-0192
Address 3817 Larchmont Lane Suite B Baltimore, MD 21208
Email DR@BrightCoatInc.example

Font styles to use
Sans Serif

Requirements
Must have
• Want the background to be black and silver gradient. Will be printing on high gloss and would like for it to be rich looking.
• brochure will be 8.5x11. open minded in terms of the fold, how it looks best with the design provided will determine that. Can be bi-fold, try-fold or z-fold.
• Content for brochure:About us
• Founded in 2003, The Bright Coat Inc. was the vision of Dovid Rennick, with a commitment to becoming the premier renovator and developer of residential and commercial properties in the DMV. Today, The Bright Coat Inc. is widely respected for their gold standard in quality and efficiency and continues to grow by attracting the highest level of professionals with knowledge and experience in our field.
• The Bright Coat Inc.’s most valuable asset is our team members. The efforts they put forth are the key to meeting our standards and providing all of our valued clients with the highest quality of service. Leading our wonderful team members is a group of management like no other. With years of experience, the power to motivate and the keen eye to ensure top quality, our team of experts focus all of their energy to exceed our client’s expectations.
• Our Mission
• We strive to provide timely delivery, the highest level of quality and value on every project. We offer unsurpassed dedication to maintain our working relationships and consistently deliver the best service to ensure our clients success.
• Property Renovations
• The Bright Coat Inc. has been responsible for coordinating the construction and renovation of many projects, including all parts of a building’s interior and exterior. Well known for attention to details, quality and timely execution, The Bright Coat Inc. has managed and executed more than 4,000 turnovers and over 150 projects in the last 3 years alone.
• Renovations not only improve the appeal and marketability of your property, but also add value. Interior and exterior renovations help make any property more functional, energy-efficient and enable you to keep up with what your market demands. From the smallest change of a door knob to a complete kitchen overhaul, these are the things that make all the difference in your property. We are committed to deliver great value, and we do that by ensuring that our experts are involved in the renovation process, providing input and quality maintenance throughout the entire renovation.
• Services Include
• Painting
• Flooring
• Sub-Flooring
• Crown molding
• Siding & Wood Replacement
• Trim & Carpentry Work
• Punches
• Decks
• Power wash
• Concrete & Paving
• Turnovers including plumbing and electric
• Kitchen overhauls
• We offer first time clients a free apartment paint or punch on us to show you the quality you can always expect!
• Call today to schedule your first-time paint or punch at 410-555-0192.

```html
<!DOCTYPE html>
<html lang="en">
<head>
<meta charset="utf-8">
<title>The Bright Coat Inc. – Tri-fold Brochure</title>
<link href="https://fonts.googleapis.com/css2?family=Michroma&family=Lato:wght@400;700&display=swap" rel="stylesheet">
<style>
  :root{
    --canvas:#c6ecfb;
    --black:#0e0e0e;
    --charcoal:#2a2a2a;
    --silver:#c9c9c9;
    --silver-light:#f1f1f1;
    --grey-band:#6f7074;
    --text:#ffffff;
    --text-soft:#d9d9d9;
    --ink:#111111;
  }
  *{margin:0;padding:0;box-sizing:border-box}
  html,body{width:1200px;height:1200px;overflow:hidden}
  body{background:var(--canvas);font-family:'Lato',sans-serif;color:var(--text)}
  .spread{position:absolute;left:40px;width:1120px;height:560px;box-shadow:0 10px 30px rgba(0,0,0,.25)}
  .spread--outside{top:30px}
  .spread--inside{top:610px}
  .spread__art{position:absolute;inset:0}
  .block{position:absolute}
  .heading{font-family:'Michroma',sans-serif;font-size:10px;letter-spacing:.5px;text-transform:uppercase;margin-bottom:8px}
  .body-copy{font-size:8.4px;line-height:11px;color:var(--text-soft);text-align:justify}
  .body-copy p{margin-bottom:7px}
  .wordmark{display:flex;flex-direction:column;align-items:center;gap:6px}
  .wordmark__dot{width:34px;height:34px;border-radius:50%;background:var(--silver-light)}
  .wordmark__name{font-family:'Michroma',sans-serif;font-size:15px;color:var(--text);letter-spacing:.5px}
  .offer{text-align:center;font-size:13px;line-height:16px}
  .offer .caps{font-family:'Michroma',sans-serif;color:var(--silver);font-size:12px;letter-spacing:.5px}
  .offer .big{font-size:15px}
  .phone{display:flex;align-items:center;justify-content:center;gap:7px;font-family:'Michroma',sans-serif;font-size:13px;margin-top:14px}
  .contact{text-align:center;font-size:8.5px;font-weight:700}
  .contact__row{display:flex;flex-direction:column;align-items:center;gap:3px;margin-bottom:10px}
  .tagline{position:absolute;left:880px;width:240px;top:478px;text-align:center;font-family:'Michroma',sans-serif;color:var(--ink)}
  .tagline__top{font-size:19px;line-height:20px}
  .tagline__bottom{font-size:13px;line-height:16px}
  .site-band{position:absolute;left:895px;width:225px;top:530px;text-align:center;font-size:8px;letter-spacing:2.5px;color:var(--silver-light)}
  .services{display:grid;grid-template-columns:1fr 1fr;row-gap:34px;column-gap:14px}
  .service{display:flex;flex-direction:column;align-items:center;text-align:center;gap:6px;font-family:'Michroma',sans-serif;font-size:7.5px;line-height:10px;color:var(--text-soft)}
  .service svg{width:26px;height:22px}
</style>
</head>
<body>

<!-- OUTSIDE SPREAD -->
<section class="spread spread--outside" aria-label="Brochure outside">
  <svg class="spread__art" viewBox="0 0 1120 560" width="1120" height="560">
    <defs>
      <linearGradient id="richBlack" x1="0" y1="0" x2="1" y2="1">
        <stop offset="0" stop-color="#050505"/>
        <stop offset=".55" stop-color="#1c1c1c"/>
        <stop offset="1" stop-color="#3a3a3a"/>
      </linearGradient>
      <linearGradient id="interiorTones" x1="0" y1="0" x2="1" y2="1">
        <stop offset="0" stop-color="#e7e4dc"/>
        <stop offset=".6" stop-color="#bdb6a8"/>
        <stop offset="1" stop-color="#8a8272"/>
      </linearGradient>
      <linearGradient id="kitchenTones" x1="0" y1="0" x2="0" y2="1">
        <stop offset="0" stop-color="#d9cbb0"/>
        <stop offset=".5" stop-color="#eee9df"/>
        <stop offset="1" stop-color="#7d7a75"/>
      </linearGradient>
      <linearGradient id="silverBand" x1="0" y1="0" x2="1" y2="0">
        <stop offset="0" stop-color="#ffffff"/>
        <stop offset="1" stop-color="#cfcfcf"/>
      </linearGradient>
    </defs>
    <rect width="1120" height="560" fill="url(#richBlack)"/>
    <line x1="373" y1="0" x2="373" y2="560" stroke="#000" stroke-opacity=".5"/>
    <line x1="747" y1="0" x2="747" y2="560" stroke="#000" stroke-opacity=".5"/>

    <path d="M0 0 H330 C305 120 200 205 0 225 Z" fill="url(#interiorTones)" role="img" aria-label="Photo of an interior hallway under renovation"/>
    <path d="M336 0 C310 125 205 212 0 232" fill="none" stroke="var(--silver)" stroke-width="4"/>

    <line x1="420" y1="235" x2="700" y2="235" stroke="#555"/>

    <path d="M1120 150 C990 150 880 250 870 470 L1120 470 Z" fill="url(#kitchenTones)" role="img" aria-label="Photo of a renovated kitchen with white cabinets and tiled backsplash"/>
    <path d="M870 470 H1120 V515 H878 Z" fill="url(#silverBand)"/>
    <path d="M878 515 H1120 V560 H895 Z" fill="var(--grey-band)"/>
    <path d="M1120 140 C982 142 868 245 862 470 C862 510 872 540 887 560" fill="none" stroke="var(--silver)" stroke-width="4"/>
  </svg>

  <div class="block" style="left:20px;top:250px;width:325px">
    <h2 class="heading">About Us</h2>
    <div class="body-copy">
      <p>Founded in 2003, The Bright Coat Inc. was the vision of Dovid Rennick, with a commitment to becoming the premier renovator and developer of residential and commercial properties in the DMV. Today, The Bright Coat Inc. is widely respected for their gold standard in quality and efficiency and continues to grow by attracting the highest level of professionals with knowledge and experience in our field.</p>
      <p>The Bright Coat Inc.’s most valuable asset is our team members. The efforts they put forth are the key to meeting our standards and providing all of our valued clients with the highest quality of service. Leading our wonderful team members is a group of management like no other. With years of experience, the power to motivate and the keen eye to ensure top quality, our team of experts focus all of their energy to exceed our client’s expectations.</p>
    </div>
    <h2 class="heading" style="margin-top:4px">Our Mission</h2>
    <div class="body-copy">
      <p>We strive to provide timely delivery, the highest level of quality and value on every project. We offer unsurpassed dedication to maintain our working relationships and consistently deliver the best service to ensure our clients success.</p>
    </div>
  </div>

  <div class="block offer" style="left:373px;top:70px;width:374px">
    <div class="caps big">We Offer</div>
    <div>first time clients a</div>
    <div class="caps">Free Apartment</div>
    <div>paint or punch on us</div>
    <div class="caps" style="font-size:9.5px">To show you the quality</div>
    <div style="font-weight:700">you can always expect!</div>
  </div>

  <div class="block offer" style="left:373px;top:255px;width:374px">
    <div class="caps big">Call Today</div>
    <div>to schedule your</div>
    <div class="caps">First-Time</div>
    <div>paint or punch at</div>
    <div class="phone">
      <svg width="14" height="14" viewBox="0 0 24 24" aria-hidden="true"><path d="M6.6 10.8a15 15 0 0 0 6.6 6.6l2.2-2.2a1 1 0 0 1 1-.25 11.4 11.4 0 0 0 3.6.6 1 1 0 0 1 1 1V20a1 1 0 0 1-1 1A17 17 0 0 1 3 4a1 1 0 0 1 1-1h3.5a1 1 0 0 1 1 1c0 1.25.2 2.45.6 3.6a1 1 0 0 1-.25 1Z" fill="#fff"/></svg>
      410-555-0192
    </div>
  </div>

  <div class="block wordmark" style="left:373px;top:380px;width:374px">
    <span class="wordmark__dot"></span>
    <span class="wordmark__name" style="font-size:12px">THE BRIGHT COAT</span>
  </div>

  <div class="block contact" style="left:373px;top:455px;width:374px">
    <div class="contact__row">
      <svg width="11" height="9" viewBox="0 0 22 16" aria-hidden="true"><rect x="1" y="1" width="20" height="14" rx="2" fill="none" stroke="#fff" stroke-width="2"/><path d="M1 2l10 7 10-7" fill="none" stroke="#fff" stroke-width="2"/></svg>
      hello@brightcoatinc.example
    </div>
    <div class="contact__row">
      <svg width="11" height="11" viewBox="0 0 22 22" aria-hidden="true"><circle cx="11" cy="11" r="9" fill="none" stroke="#fff" stroke-width="2"/><path d="M2 11h18M11 2c-4 5-4 13 0 18M11 2c4 5 4 13 0 18" fill="none" stroke="#fff" stroke-width="1.6"/></svg>
      www.brightcoatinc.example
    </div>
    <div class="contact__row">
      <svg width="11" height="10" viewBox="0 0 22 20" aria-hidden="true"><path d="M11 1 1 10h3v9h5v-6h4v6h5v-9h3Z" fill="#fff"/></svg>
      3817 Larchmont Lane Baltimore, Maryland
    </div>
  </div>

  <div class="block wordmark" style="left:747px;top:40px;width:373px">
    <span class="wordmark__dot"></span>
    <span class="wordmark__name">THE BRIGHT COAT</span>
  </div>

  <div class="tagline">
    <div class="tagline__top">A STEP</div>
    <div class="tagline__bottom">Above The Rest</div>
  </div>
  <div class="site-band">www.brightcoatinc.example</div>
</section>

<!-- INSIDE SPREAD -->
<section class="spread spread--inside" aria-label="Brochure inside">
  <svg class="spread__art" viewBox="0 0 1120 560" width="1120" height="560">
    <defs>
      <linearGradient id="richBlack2" x1="0" y1="0" x2="1" y2="1">
        <stop offset="0" stop-color="#050505"/>
        <stop offset=".55" stop-color="#1c1c1c"/>
        <stop offset="1" stop-color="#3a3a3a"/>
      </linearGradient>
      <linearGradient id="roomTones" x1="0" y1="0" x2="1" y2="1">
        <stop offset="0" stop-color="#f2f1ee"/>
        <stop offset=".6" stop-color="#c9c6c0"/>
        <stop offset="1" stop-color="#7b7770"/>
      </linearGradient>
      <linearGradient id="deckTones" x1="0" y1="0" x2="1" y2="1">
        <stop offset="0" stop-color="#b07356"/>
        <stop offset=".5" stop-color="#d8c28e"/>
        <stop offset="1" stop-color="#8a5a45"/>
      </linearGradient>
    </defs>
    <rect width="1120" height="560" fill="url(#richBlack2)"/>
    <line x1="373" y1="0" x2="373" y2="560" stroke="#000" stroke-opacity=".5"/>
    <line x1="747" y1="0" x2="747" y2="560" stroke="#000" stroke-opacity=".5"/>

    <path d="M0 345 C150 312 300 322 420 370 C450 400 470 470 480 560 H0 Z" fill="url(#roomTones)" role="img" aria-label="Photo of a freshly drywalled room ready for paint"/>
    <path d="M0 338 C150 305 305 315 426 365" fill="none" stroke="var(--silver)" stroke-width="4"/>

    <path d="M560 560 C690 430 890 300 1120 228 V560 Z" fill="url(#deckTones)" role="img" aria-label="Photo of a new wooden deck on a brick house"/>
    <path d="M552 560 C684 424 886 293 1120 220" fill="none" stroke="var(--silver)" stroke-width="4"/>
  </svg>

  <div class="block" style="left:20px;top:22px;width:330px">
    <h2 class="heading">Property Renovations</h2>
    <div class="body-copy">
      <p>The Bright Coat Inc. has been responsible for coordinating the construction and renovation of many projects, including all parts of a building’s interior and exterior. Well known for attention to details, quality and timely execution, The Bright Coat Inc. has managed and executed more than 4,000 turnovers and over 150 projects in the last 3 years alone.</p>
      <p>Renovations not only improve the appeal and marketability of your property, but also add value. Interior and exterior renovations help make any property more functional, energy-efficient and enable you to keep up with what your market demands. From the smallest change of a door knob to a complete kitchen overhaul, these are the things that make all the difference in your property. We are committed to deliver great value, and we do that by ensuring that our experts are involved in the renovation process, providing input and quality maintenance throughout the entire renovation.</p>
    </div>
  </div>

  <div class="block" style="left:393px;top:22px;width:334px">
    <h2 class="heading" style="text-align:center;margin-bottom:24px">Services Include</h2>
    <div class="services">
      <div class="service"><svg viewBox="0 0 26 22" aria-hidden="true"><rect x="3" y="3" width="16" height="7" rx="1" fill="none" stroke="#fff" stroke-width="1.6"/><path d="M19 6h3v6h-9v8" fill="none" stroke="#fff" stroke-width="1.6"/></svg>Painting</div>
      <div class="service"><svg viewBox="0 0 26 22" aria-hidden="true"><path d="M2 16 13 10l11 6-11 4Z" fill="none" stroke="#fff" stroke-width="1.6"/></svg>Flooring</div>
      <div class="service"><svg viewBox="0 0 26 22" aria-hidden="true"><path d="M2 14 13 8l11 6-11 5Z M2 10l11-6 11 6" fill="none" stroke="#fff" stroke-width="1.6"/></svg>Sub-Flooring</div>
      <div class="service"><svg viewBox="0 0 26 22" aria-hidden="true"><path d="M3 8c6 0 8 6 20 6" fill="none" stroke="#fff" stroke-width="2"/></svg>Crown molding</div>
      <div class="service"><svg viewBox="0 0 26 22" aria-hidden="true"><rect x="4" y="3" width="18" height="16" fill="none" stroke="#fff" stroke-width="1.6"/><path d="M4 19 22 3M4 11l8-8M14 19l8-8" stroke="#fff" stroke-width="1.2"/></svg>Siding &amp; Wood<br>Replacement</div>
      <div class="service"><svg viewBox="0 0 26 22" aria-hidden="true"><path d="M4 4l18 14M22 4 4 18" stroke="#fff" stroke-width="2"/></svg>Trim &amp; Carpentry<br>Work</div>
    </div>
  </div>

  <div class="block" style="left:767px;top:30px;width:333px">
    <div class="services" style="row-gap:26px">
      <div class="service"><svg viewBox="0 0 26 22" aria-hidden="true"><path d="M3 8h14v5H3Z M17 10h6 M8 13v6" fill="none" stroke="#fff" stroke-width="1.6"/></svg>Punches</div>
      <div class="service"><svg viewBox="0 0 26 22" aria-hidden="true"><rect x="3" y="4" width="20" height="12" fill="none" stroke="#fff" stroke-width="1.6"/><path d="M7 4v12M11 4v12M15 4v12M19 4v12" stroke="#fff" stroke-width="1.2"/></svg>Decks</div>
      <div class="service"><svg viewBox="0 0 26 22" aria-hidden="true"><path d="M9 3h8v4l-2 2v10H11V9L9 7Z" fill="none" stroke="#fff" stroke-width="1.6"/></svg>Power wash</div>
      <div class="service"><svg viewBox="0 0 26 22" aria-hidden="true"><path d="M4 14a9 8 0 0 1 18 0Z M4 17h18" fill="none" stroke="#fff" stroke-width="1.6"/></svg>Concrete &amp; Paving</div>
      <div class="service"><svg viewBox="0 0 26 22" aria-hidden="true"><path d="M4 18V8h8v6h10" fill="none" stroke="#fff" stroke-width="2"/></svg>Turnovers including<br>plumbing and electric</div>
      <div class="service"><svg viewBox="0 0 26 22" aria-hidden="true"><rect x="3" y="5" width="20" height="13" fill="none" stroke="#fff" stroke-width="1.6"/><path d="M3 10h20M10 10v8" stroke="#fff" stroke-width="1.2"/></svg>Kitchen overhauls</div>
    </div>
  </div>
</section>

</body>
</html>
```